Make the invisible visible.... and attractive

I have an online course at http://www.brightlanepath.com/Begin-today-here.html. I need an attractive graphic to sell the product. The course is a series of video, audio and handout materials set out in 32 lessons and has a free one year confidence course as a bonus.

Target Market(s)

Individuals who have problems with fear or anxiety.

Industry/Entity Type

Audio

```html
<!DOCTYPE html>
<html lang="en">
<head>
<meta charset="utf-8">
<title>Bright Lane Course Online – Start Right Now</title>
<link href="https://fonts.googleapis.com/css2?family=Raleway:wght@300;400;500;600;700&display=swap" rel="stylesheet">
<style>
  :root {
    --olive: #3f4c1f;
    --purple: #7b3fb8;
    --purple-deep: #5e2a93;
    --lavender: #c9a8ea;
    --seal: #8a4cc4;
    --seal-dark: #6b32a3;
    --white: #ffffff;
    --panel: rgba(255, 255, 255, 0.78);
    --button-top: #ffffff;
    --button-bottom: #dcdcd4;
  }
  * { margin: 0; padding: 0; box-sizing: border-box; }
  html, body { width: 1200px; height: 666px; overflow: hidden; background: #ffffff; }
  .banner {
    position: relative;
    width: 1200px;
    height: 666px;
    overflow: hidden;
    font-family: "Raleway", sans-serif;
  }
  .scene-photo {
    position: absolute;
    inset: 0;
    background:
      radial-gradient(ellipse 320px 380px at 1000px 260px, #c9b3a0 0%, #b9a6c9 45%, rgba(220,215,210,0) 75%),
      linear-gradient(180deg, #d8d6d2 0%, #ebe8e3 40%, #f4f1ec 62%, #e9e5df 100%);
  }
  .feature-panel {
    position: absolute;
    left: 0;
    top: 36px;
    width: 442px;
    height: 302px;
    background: var(--panel);
    padding: 30px 0 0 30px;
    color: var(--olive);
    text-transform: uppercase;
    line-height: 1;
  }
  .feature-panel .title-top { font-size: 76px; font-weight: 500; letter-spacing: -1px; }
  .feature-panel .title-sub { font-size: 54px; font-weight: 500; margin: 4px 0 0 106px; }
  .feature-panel .lessons { font-size: 48px; font-weight: 400; margin: 14px 0 0 14px; }
  .feature-panel .formats { font-size: 34px; font-weight: 400; margin: 6px 0 0 72px; line-height: 1.12; }
  .bonus-seal {
    position: absolute;
    left: 492px;
    top: -14px;
    width: 290px;
    height: 204px;
  }
  .bonus-seal svg { position: absolute; inset: 0; }
  .bonus-seal .seal-text {
    position: absolute;
    inset: 0;
    display: flex;
    flex-direction: column;
    align-items: center;
    justify-content: center;
    color: var(--white);
    text-transform: uppercase;
    line-height: 1;
    padding-top: 10px;
  }
  .bonus-seal .free { font-size: 62px; font-weight: 700; }
  .bonus-seal .bonus { font-size: 26px; font-weight: 500; margin-top: 6px; }
  .wave { position: absolute; left: 0; top: 0; width: 1200px; height: 666px; }
  .pitch {
    position: absolute;
    left: 22px;
    top: 482px;
    width: 860px;
    color: var(--white);
    font-size: 19px;
    font-weight: 500;
    line-height: 1.48;
  }
  .cta-button {
    position: absolute;
    left: 896px;
    top: 466px;
    width: 288px;
    height: 172px;
    border-radius: 26px;
    background: linear-gradient(180deg, var(--button-top) 0%, #f3f3ee 55%, var(--button-bottom) 100%);
    box-shadow: 0 4px 10px rgba(40, 10, 70, 0.45);
    color: var(--olive);
    text-align: center;
    text-transform: uppercase;
    padding-top: 24px;
    line-height: 1;
  }
  .cta-button .start { display: block; font-size: 66px; font-weight: 600; }
  .cta-button .right-now { display: block; font-size: 40px; font-weight: 600; margin-top: 8px; }
  .cta-button .deadline { display: block; font-size: 16px; font-weight: 600; margin-top: 8px; }
</style>
</head>
<body>
<main class="banner">
  <div class="scene-photo" role="img" aria-label="Photo of a smiling young woman in a purple top lying on a white rug, working on a laptop in a bright living room"></div>

  <section class="feature-panel">
    <div class="title-top">Online</div>
    <div class="title-sub">Course</div>
    <div class="lessons">32 Lessons</div>
    <div class="formats">Video, Audio<br>and Handouts</div>
  </section>

  <div class="bonus-seal">
    <svg viewBox="0 0 290 204" aria-hidden="true">
      <ellipse cx="145" cy="102" rx="132" ry="96" fill="var(--seal-dark)"/>
      <ellipse cx="145" cy="100" rx="118" ry="84" fill="var(--seal)"/>
    </svg>
    <div class="seal-text">
      <span class="free">Free</span>
      <span class="bonus">Bonus<br>Courses</span>
    </div>
  </div>

  <svg class="wave" viewBox="0 0 1200 666" aria-hidden="true">
    <path d="M0 340 C 300 400, 700 450, 1200 460 L1200 666 L0 666 Z" fill="var(--lavender)" opacity="0.7"/>
    <path d="M0 360 C 320 420, 720 470, 1200 470 L1200 666 L0 666 Z" fill="#ffffff" opacity="0.55"/>
    <path d="M0 438 C 260 470, 520 480, 760 470 C 950 460, 1100 440, 1200 432 L1200 666 L0 666 Z" fill="var(--purple)"/>
    <path d="M0 600 C 400 640, 800 620, 1200 590 L1200 666 L0 666 Z" fill="var(--purple-deep)" opacity="0.5"/>
  </svg>

  <p class="pitch">Develop powerful emotional resilience quickly and easily. The Bright Lane Course Online gives you everything you need to be calm and composed in any situation. Start right now. By the end of today you will have everything you need to return you to a calm and composed state, easily.</p>

  <div class="cta-button">
    <span class="start">Start</span>
    <span class="right-now">Right Now</span>
    <span class="deadline">By the end of today...</span>
  </div>
</main>
</body>
</html>
```